Grillo Dash

I am looking for a Food Truck wrap with a Philly Cheesesteak Sandwich,Cheese curds, French, and Corn dogs.

Font styles to use
Sans Serif

Colors
59FF00
82FF00
B8FF75
E3FFCB
F4FFEA
FFF300
FFF600
FEFA6F
FFFEC7
FFFEE8
FFC000
F8CF3A
FAE287
FDF2CF
FEFAEE
F0912C
F2A743
F7CA91
FBE8D2
FDF5EE

```html
<!DOCTYPE html>
<html lang="en">
<head>
<meta charset="utf-8">
<title>Grillo Dash – Food Truck Wrap</title>
<link href="https://fonts.googleapis.com/css2?family=Anton&family=Dancing+Script:wght@600&family=Lobster&display=swap" rel="stylesheet">
<style>
  :root{
    --page:#ffffff;
    --orange-light:#F2A743;
    --orange:#F0912C;
    --orange-deep:#EE5F2C;
    --ink:#0d0d0d;
    --ink-soft:#1b1b1b;
    --gold:#FFC000;
    --cream:#FFFEC7;
    --peach:#FBE8D2;
    --white:#ffffff;
    --tag-red:#E8351E;
  }
  *{margin:0;padding:0;box-sizing:border-box}
  html,body{width:966px;height:1200px;overflow:hidden;background:var(--page)}
  body{position:relative;font-family:"Anton",sans-serif}

  /* ---------- wrap panel ---------- */
  .wrap-panel{
    position:absolute;left:33px;top:170px;width:900px;height:374px;overflow:hidden;
    background:linear-gradient(90deg,var(--orange) 0%,var(--orange-light) 25%,var(--orange) 45%,var(--orange-deep) 68%);
  }
  .wrap-panel .shapes{position:absolute;inset:0}
  .panel-name{
    position:absolute;left:147px;top:84px;width:360px;text-align:center;
    font-family:"Anton",sans-serif;font-size:56px;line-height:1;letter-spacing:1px;color:var(--ink-soft);
  }
  .panel-tagline{
    position:absolute;left:137px;top:156px;width:380px;text-align:center;
    font-family:"Lobster",sans-serif;font-size:11px;line-height:1.2;color:var(--tag-red);
  }
  .panel-web{
    position:absolute;left:147px;top:214px;width:360px;text-align:center;
    font-family:"Anton",sans-serif;font-size:25px;line-height:1.2;color:var(--white);letter-spacing:.3px;
  }
  .panel-phone{
    position:absolute;left:147px;top:254px;width:360px;text-align:center;
    font-family:"Anton",sans-serif;font-size:28px;line-height:1.2;color:var(--cream);letter-spacing:.5px;
  }
  .panel-delivery{
    position:absolute;left:227px;top:302px;width:200px;text-align:center;
    font-family:"Dancing Script",cursive;font-size:18px;line-height:1.2;color:var(--cream);
  }

  .tag-eat{position:absolute;left:566px;top:30px;transform:rotate(-22deg);transform-origin:left top}
  .tag-eat div{font-family:"Anton",sans-serif;color:var(--white);font-size:22px;line-height:1;padding:4px 10px}
  .tag-eat .eat-top{background:var(--gold)}
  .tag-eat .eat-bottom{background:var(--orange);margin-left:28px;width:max-content}

  .tag-super{
    position:absolute;left:706px;top:14px;font-family:"Anton",sans-serif;font-size:21px;line-height:1.05;color:var(--white);
  }
  .tag-super .gold{color:var(--gold)}
  .tag-super .l1,.tag-super .l3{margin-left:3px}

  .tag-offer{
    position:absolute;right:4px;top:30px;text-align:right;font-family:"Anton",sans-serif;line-height:1;color:var(--white);
  }
  .tag-offer .o1{font-size:12px}
  .tag-offer .o2{font-size:21px;color:var(--gold)}
  .tag-offer .o3{font-size:12px}
  .tag-offer .o4{font-size:12px;color:var(--gold)}

  .photo{position:absolute;border-radius:6px}
  .photo-steak{left:612px;top:104px;width:252px;height:128px;
    background:linear-gradient(135deg,#6b3a1e 0%,#d89b5a 35%,#8a4a22 60%,#f2b84a 100%);}
  .photo-curds{left:608px;top:238px;width:145px;height:104px;border-radius:50%;
    background:radial-gradient(circle at 50% 50%,#f7c25a 0%,#e8a23a 55%,#f1ede6 80%,#2a2a2a 100%);}
  .photo-corndogs{left:760px;top:238px;width:136px;height:128px;
    background:linear-gradient(160deg,#c98a3c 0%,#8b3a1c 45%,#f0c24a 75%,#b87a3a 100%);}

  /* ---------- standalone name block ---------- */
  .brand-block{position:absolute;left:0;top:740px;width:966px;height:240px}
  .brand-name{
    position:absolute;left:0;top:40px;width:966px;text-align:center;
    font-family:"Anton",sans-serif;font-size:92px;line-height:1.1;letter-spacing:2px;color:var(--ink-soft);
  }
  .brand-tagline{
    position:absolute;left:0;top:164px;width:966px;text-align:center;
    font-family:"Lobster",sans-serif;font-size:16px;line-height:1.2;color:var(--tag-red);
  }
</style>
</head>
<body>

<section class="wrap-panel">
  <svg class="shapes" width="900" height="374" viewBox="0 0 900 374">
    <path d="M480 0 L900 0 L900 374 L482 374 L488 340 L474 318 L496 296 L486 270 L508 250 L500 226 L522 206 L514 180 L536 160 L528 134 L556 118 L548 92 L572 76 L560 52 L590 34 L568 18 L596 4 Z" fill="var(--ink)"/>
    <path d="M0 60 L110 64 Q120 200 200 250 Q300 300 460 300 L460 374 L0 374 Z" fill="var(--orange-light)" opacity=".35"/>
    <ellipse cx="210" cy="12" rx="18" ry="16" fill="none" stroke="var(--peach)" stroke-opacity=".45" stroke-width="2"/>
    <ellipse cx="210" cy="12" rx="10" ry="9" fill="none" stroke="var(--peach)" stroke-opacity=".45" stroke-width="2"/>
    <ellipse cx="462" cy="268" rx="20" ry="26" fill="none" stroke="var(--peach)" stroke-opacity=".45" stroke-width="2"/>
    <ellipse cx="462" cy="268" rx="12" ry="16" fill="none" stroke="var(--peach)" stroke-opacity=".45" stroke-width="2"/>
    <path d="M510 146 a14 16 0 0 0 0 30" fill="none" stroke="var(--peach)" stroke-opacity=".45" stroke-width="2"/>
    <g fill="var(--peach)" opacity=".5">
      <circle cx="372" cy="6" r="2.5"/><circle cx="384" cy="6" r="2.5"/><circle cx="396" cy="6" r="2.5"/><circle cx="408" cy="6" r="2.5"/>
      <circle cx="372" cy="20" r="2.5"/><circle cx="384" cy="20" r="2.5"/><circle cx="396" cy="20" r="2.5"/><circle cx="408" cy="20" r="2.5"/>
      <circle cx="372" cy="34" r="2.5"/><circle cx="384" cy="34" r="2.5"/><circle cx="396" cy="34" r="2.5"/><circle cx="408" cy="34" r="2.5"/>
      <circle cx="172" cy="354" r="2.5"/><circle cx="184" cy="354" r="2.5"/><circle cx="196" cy="354" r="2.5"/><circle cx="208" cy="354" r="2.5"/><circle cx="220" cy="354" r="2.5"/><circle cx="232" cy="354" r="2.5"/><circle cx="244" cy="354" r="2.5"/>
      <circle cx="172" cy="366" r="2.5"/><circle cx="184" cy="366" r="2.5"/><circle cx="196" cy="366" r="2.5"/><circle cx="208" cy="366" r="2.5"/><circle cx="220" cy="366" r="2.5"/><circle cx="232" cy="366" r="2.5"/><circle cx="244" cy="366" r="2.5"/>
    </g>
    <path d="M680 26 L702 30 L682 36 Z M688 46 L702 32 L694 50 Z" fill="var(--gold)"/>
    <path d="M776 72 L754 76 L774 82 Z M768 62 L754 74 L764 58 Z" fill="var(--gold)"/>
    <path d="M900 0 L842 58 L900 118" fill="none" stroke="var(--orange-deep)" stroke-width="4"/>
  </svg>

  <div class="panel-name">GRILLO DASH</div>
  <div class="panel-tagline">Philly Cheesesteak Sandwich, Cheese curds, French, and Corn dogs</div>
  <div class="panel-web">www.GrilloDash.com</div>
  <div class="panel-phone">(555) 014 27390</div>
  <div class="panel-delivery">Free Delivery</div>

  <div class="tag-eat"><div class="eat-top">LET'S</div><div class="eat-bottom">EAT</div></div>
  <div class="tag-super"><div class="l1">SUPER</div><div class="gold">DELICIOUS</div><div class="l3">FOOD</div></div>
  <div class="tag-offer"><div class="o1">SPCIAL</div><div class="o2">OFFER</div><div class="o3">PRICE</div><div class="o4">25$</div></div>

  <div class="photo photo-steak" role="img" aria-label="Photo of a Philly cheesesteak sandwich with fries and ketchup on a wooden board"></div>
  <div class="photo photo-curds" role="img" aria-label="Photo of a plate of fried cheese curds with dipping sauce"></div>
  <div class="photo photo-corndogs" role="img" aria-label="Photo of assorted corn dogs with mustard and ketchup"></div>
</section>

<section class="brand-block">
  <div class="brand-name">GRILLO DASH</div>
  <div class="brand-tagline">Philly Cheesesteak Sandwich, Cheese curds, French, and Corn dogs</div>
</section>

</body>
</html>
```